Brightpath Dental Studio

Please go to www.brightpathdentalstudio.example and obtain the current company logo.
Doctors name are
Marita Velbonne, DDS
Denis Kalb, DMD
Addresses are
318 Larchmont Ave
Teaneck, NJ 07666
201-555-0147
And
872 14th St.
West New York, NJ 07093
201-555-0182
Theme of the business card should feel modrrn and similar to the website.
Front side should include company logo, doctors name, addresses, phone numbers.
Back of the card should include blank lines for patient's name. Date and time for next scheduled appointment. And notice of 24-hr cancellation courtesy policy.
Dental

```html
<!DOCTYPE html>
<html lang="en">
<head>
<meta charset="utf-8">
<title>Brightpath Dental Studio – Business Card</title>
<link href="https://fonts.googleapis.com/css2?family=Arimo:wght@400;700&display=swap" rel="stylesheet">
<style>
  :root {
    --navy: #0f1a4d;
    --white: #ffffff;
    --ink: #111111;
    --stage: #e9e7e4;
    --photo-light: #e6ddd2;
    --photo-mid: #c9b4a0;
    --photo-warm: #e5734f;
  }
  * { box-sizing: border-box; margin: 0; padding: 0; }
  html, body { width: 1200px; height: 1200px; overflow: hidden; }
  body {
    background: var(--stage);
    font-family: "Arimo", Arial, sans-serif;
    position: relative;
  }
  .card {
    position: absolute;
    left: 130px;
    width: 940px;
    height: 537px;
    background: var(--white);
    overflow: hidden;
    box-shadow: 0 6px 18px rgba(0,0,0,0.18);
  }
  .card--front { top: 42px; }
  .card--back { top: 621px; }

  /* Front */
  .doctors-band {
    position: absolute; top: 0; left: 0; right: 0; height: 72px;
    background: var(--navy); color: var(--white);
    display: flex; align-items: center; justify-content: center; gap: 30px;
    font-size: 27px; letter-spacing: 0.3px;
  }
  .photo-area {
    position: absolute; top: 72px; left: 0; right: 0; height: 325px;
    background:
      radial-gradient(ellipse 30% 55% at 75% 40%, #e8c2a6 0%, rgba(232,194,166,0) 70%),
      radial-gradient(ellipse 30% 35% at 55% 95%, var(--photo-warm) 0%, rgba(229,115,79,0) 75%),
      linear-gradient(90deg, var(--photo-light) 0%, #d8d3c9 45%, var(--photo-mid) 100%);
  }
  .front-logo {
    position: absolute; top: 120px; left: 40px;
    display: flex; align-items: center; gap: 14px;
    color: var(--ink); font-size: 38px; font-weight: 700;
  }
  .logo-dot {
    width: 30px; height: 30px; border-radius: 50%;
    background: var(--navy); flex: none;
  }
  .contact-band {
    position: absolute; bottom: 0; left: 0; right: 0; height: 140px;
    background: var(--navy); color: var(--white);
    display: flex;
  }
  .location {
    flex: 1; display: flex; flex-direction: column;
    align-items: center; justify-content: center; gap: 6px;
  }
  .location + .location { border-left: 4px solid var(--white); }
  .location__address { font-size: 21px; }
  .location__phone { font-size: 52px; letter-spacing: 0.5px; }

  /* Back */
  .appointment {
    position: absolute; top: 40px; left: 44px; color: var(--navy);
  }
  .appointment__label { font-size: 34px; }
  .appointment__label--second { margin-top: 36px; }
  .appointment__note { font-size: 21px; margin-top: 4px; }
  .back-logo {
    position: absolute; top: 300px; left: 0; right: 0;
    display: flex; align-items: center; justify-content: center; gap: 20px;
    color: var(--ink); font-size: 60px; font-weight: 700;
  }
  .back-logo .logo-dot { width: 46px; height: 46px; }
  .policy-band {
    position: absolute; bottom: 0; left: 0; right: 0; height: 72px;
    background: var(--navy); color: var(--white);
    display: flex; align-items: center; justify-content: center;
    font-size: 24px;
  }
</style>
</head>
<body>
  <section class="card card--front">
    <div class="doctors-band">
      <span>Dr. Marita Velbonne, DDS</span>
      <span>&amp;</span>
      <span>Dr. Denis Kalb, DMD</span>
    </div>
    <div class="photo-area" role="img" aria-label="Photograph of a smiling patient in a bright dental office"></div>
    <div class="front-logo">
      <span class="logo-dot"></span>
      <span>Brightpath Dental Studio</span>
    </div>
    <div class="contact-band">
      <div class="location">
        <span class="location__address">872 14th St. West New York, NJ 07093</span>
        <span class="location__phone">201-555-0182</span>
      </div>
      <div class="location">
        <span class="location__address">318 Larchmont Ave Teaneck, NJ 07666</span>
        <span class="location__phone">201-555-0147</span>
      </div>
    </div>
  </section>

  <section class="card card--back">
    <div class="appointment">
      <p class="appointment__label">Patient's name</p>
      <p class="appointment__label appointment__label--second">Date and time</p>
      <p class="appointment__note">(for next scheduled appointment)</p>
    </div>
    <div class="back-logo">
      <span class="logo-dot"></span>
      <span>Brightpath Dental Studio</span>
    </div>
    <div class="policy-band">24-hours cancellation courtesy policy</div>
  </section>
</body>
</html>
```